Homemaking training schools needs a Business Card design

Designer, Hello!

No special requirements, good-looking enough.
--------------------------------------------------------------------------

Name: Marcus Liao
Chairman
Tel: 0574-57418263
Mobile: 13852247106
Email: kelvory@mailpond.com
Web: www.tqb2031.com
Add: No.258, LinfengJie, DaoyueQu, Ningbo, Zhejiang

LOGO
Ningbo TQB Homemaking Training School

Target Market(s)

pregnant women, mothers, infants, the elderly and families, including cleaning, cooking, nursing training.

Industry/Entity Type

Business

Contact Information for Business Card

Name: Marcus Liao
Chairman
Tel: 0574-57418263
Mobile: 13852247106
Email: kelvory@mailpond.com
Web: www.tqb2031.com

LOGO

Font styles to use
Serif
Sans Serif
Decorative

Requirements
Nice to have
• Feels: clean, specifications, safety, comfort, warmth and happiness.

```html
<!DOCTYPE html>
<html lang="en">
<head>
<meta charset="utf-8">
<title>TianQiBao Business Card</title>
<link rel="stylesheet" href="https://fonts.googleapis.com/css2?family=Lato:wght@400;700&display=swap">
<style>
  :root {
    --brand-blue: #3a7abf;
    --brand-magenta: #c4168f;
    --ink: #1f1f24;
    --paper: #ffffff;
    --backdrop: #e9eaee;
    --rule: #4a4a4a;
  }
  * { margin: 0; padding: 0; box-sizing: border-box; }
  html, body {
    width: 1200px; height: 900px; overflow: hidden;
    background: var(--backdrop);
    font-family: "Lato", Arial, sans-serif;
  }
  .sheet {
    width: 1200px; height: 900px;
    display: flex; flex-direction: column;
    align-items: center; justify-content: center; gap: 36px;
  }
  .card {
    position: relative;
    width: 640px; height: 384px;
    overflow: hidden;
    box-shadow: 0 6px 18px rgba(0,0,0,.18);
  }
  .card-back { background: var(--brand-blue); color: var(--paper); }
  .card-front { background: var(--paper); }
  .card-waves { position: absolute; inset: 0; }

  .wordmark { position: absolute; text-align: center; }
  .wordmark-name {
    font-weight: 700; font-size: 58px; letter-spacing: 0.5px; line-height: 1;
  }
  .wordmark-tagline {
    display: flex; align-items: center; gap: 10px;
    font-size: 18px; letter-spacing: 1px; margin-top: 8px;
  }
  .wordmark-tagline::before, .wordmark-tagline::after {
    content: ""; flex: 1; height: 1.5px; background: currentColor;
  }

  .card-back .wordmark { left: 0; right: 0; top: 120px; padding: 0 90px; }
  .card-back .wordmark-name { color: var(--paper); }
  .card-back .wordmark-tagline { color: var(--paper); }
  .back-web {
    position: absolute; left: 0; right: 0; top: 262px;
    text-align: center; font-size: 16px; letter-spacing: 3px;
  }

  .card-front .wordmark { left: 300px; top: 118px; width: 310px; }
  .card-front .wordmark-name { color: var(--brand-blue); font-size: 46px; }
  .card-front .wordmark-tagline { color: var(--rule); font-size: 15px; }

  .contact {
    position: absolute; left: 40px; top: 108px;
    color: var(--ink); font-size: 15px; line-height: 1.55;
  }
  .contact-address { margin-bottom: 6px; }
  .contact-row { display: flex; align-items: center; gap: 10px; }
  .contact-row svg { width: 13px; height: 13px; flex: none; fill: var(--brand-blue); }

  .person { position: absolute; left: 380px; top: 230px; }
  .person-name { color: var(--brand-blue); font-size: 30px; font-weight: 400; }
  .person-title { color: var(--ink); font-size: 18px; margin-top: 2px; }
</style>
</head>
<body>
<main class="sheet">

  <section class="card card-back">
    <div class="wordmark">
      <div class="wordmark-name">TianQiBao</div>
      <div class="wordmark-tagline">Training &amp; Services</div>
    </div>
    <div class="back-web">www.tqb2031.com</div>
  </section>

  <section class="card card-front">
    <svg class="card-waves" viewBox="0 0 640 384" preserveAspectRatio="none">
      <path d="M0 0 H330 C230 10 90 20 0 110 Z" fill="var(--brand-blue)"/>
      <path d="M0 110 C90 20 230 10 330 0 H350 C240 16 100 28 0 124 Z" fill="var(--brand-magenta)"/>
      <path d="M0 250 C140 270 220 300 300 345 C360 378 500 384 640 350 V384 H0 Z" fill="var(--brand-blue)"/>
      <path d="M290 332 C380 372 520 372 640 330 V344 C520 384 380 384 290 332 Z" fill="var(--brand-magenta)"/>
    </svg>

    <div class="contact">
      <p class="contact-address">No.258, LinfengJie<br>DaoyueQu, Ningbo, Zhejiang</p>
      <p class="contact-row">
        <svg viewBox="0 0 24 24"><path d="M6.6 10.8a15 15 0 0 0 6.6 6.6l2.2-2.2c.3-.3.7-.4 1-.2 1.1.4 2.3.6 3.6.6.6 0 1 .4 1 1V20c0 .6-.4 1-1 1A17 17 0 0 1 3 4c0-.6.4-1 1-1h3.5c.6 0 1 .4 1 1 0 1.3.2 2.5.6 3.6.1.3 0 .7-.2 1z"/></svg>
        0574-57418263
      </p>
      <p class="contact-row">
        <svg viewBox="0 0 24 24"><path d="M7 1h10a2 2 0 0 1 2 2v18a2 2 0 0 1-2 2H7a2 2 0 0 1-2-2V3a2 2 0 0 1 2-2zm0 3v14h10V4z"/></svg>
        1385-2247106
      </p>
      <p class="contact-row">
        <svg viewBox="0 0 24 24"><path d="M2 5h20v14H2zm2 2v.5l8 5 8-5V7z"/></svg>
        kelvory@mailpond.com
      </p>
      <p class="contact-row">
        <svg viewBox="0 0 24 24"><path d="M12 2a10 10 0 1 0 0 20 10 10 0 0 0 0-20zm0 2c.9 1.2 1.6 2.6 2 4h-4c.4-1.4 1.1-2.8 2-4zM4.3 14a8 8 0 0 1 0-4h3.3a16 16 0 0 0 0 4zm.9 2h3c.3 1.3.8 2.5 1.5 3.6A8 8 0 0 1 5.2 16zm3-8h-3a8 8 0 0 1 4.5-3.6C9 5.5 8.5 6.7 8.2 8zM12 20c-.9-1.2-1.6-2.6-2-4h4c-.4 1.4-1.1 2.8-2 4zm2.3-6H9.7a14 14 0 0 1 0-4h4.6a14 14 0 0 1 0 4zm.1 5.6c.7-1.1 1.2-2.300 1.5-3.6h3a8 8 0 0 1-4.5 3.6zm2-5.6a16 16 0 0 0 0-4h3.3a8 8 0 0 1 0 4z"/></svg>
        www.tqb2031.com
      </p>
    </div>

    <div class="wordmark">
      <div class="wordmark-name">TianQiBao</div>
      <div class="wordmark-tagline">Training &amp; Services</div>
    </div>

    <div class="person">
      <h1 class="person-name">Marcus Liao</h1>
      <p class="person-title">Chairman</p>
    </div>
  </section>

</main>
</body>
</html>
```